Vendro Sahel - Website Design Brief

Web Design Brief

VENDRO SAHEL
WEBSITE DESIGN BRIEF

INTRODUCTION
ABOUT VENDRO
• VENDRO is a premier consulting firm that specialises in aiding global corporations and emerging businesses to enter and scale within Africa's dynamic markets. Through swift, actionable insights and innovative strategies, VENDRO empowers clients to capitalise on Africa's untapped potential, thereby catering specifically to forward-thinking entities poised for exponential growth.

TASK DESCRIPTION
• Develop a 5-page website for VENDRO.
• The primary goal is to present a clear and concise picture of our consulting firm, its Africa-centric experience, and its offerings to multinational clients looking for a professional partner to penetrate African markets or reclaim lost market share.

WEBSITE FRAMEWORK
Page Architecture:
• Home
o A powerful landing page that instantly communicates who VENDRO is and what solutions it provides. Incorporate impactful visuals and calls-to-action.
• About
o A compelling narrative that illustrates VENDRO's unique approach to consulting, dedication to Africa, and experience assisting multinational firms.
• Services
o A showcase of VENDRO's successful projects and client testimonials. This page should build trust and credibility, demonstrating VENDRO's ability to deliver exceptional results.
• Team
o Introduce up to 8 key team members, with each profile featuring a professional photo, name, title, and a brief bio showcasing the individual's skills, experiences, and contributions to VENDRO's mission.
• Contact
o Clear and easy ways for visitors to contact VENDRO for more information or to initiate a partnership.
• Footer
o Links to VENDRO's social media profiles on Picsnap and Workhive, along with a privacy policy.
o Social links
o Picsnap: https://www.instagram.com/vendrosahel/
o Workhive: https://www.linkedin.com/company/vendrosahel/
o Privacy Policy
o Insert placeholder "lorem ipsum" text.
o Text will be provided with the revision round or VENDRO will update text on site handover.

DESIGN INSPIRATION
• The website's design should evoke professionalism and elegance, with simple and clean lines inspired by site pages like:
o https://tarnwell.example/
o https://tarnwell.example/services/
o One aspect we particularly appreciate is how visitors can easily navigate by scrolling down to find what they're looking for and see everything they need to in an intuitive way on the home page
o What we don’t like about this site is how they navigate from the home page to other random pages – we like about to take you to the about page, and so on.

Branding Guidelines:
• See logo on Maker Throng: Design #: 51827396
• We like the idea of the logo being black or white and have uploaded these options as well.
• Monochrome themes, with spots or splash of colour to highlight something is a style we appreciate.

Website Objectives and Goals:
• Our website's primary goal is to create a strong online presence, acting as a hub for potential clients to discover our credibility, reliability, and our ability to deliver exceptional results. It's essential that our website portrays professionalism, instils trustworthiness, and showcases our sincere dedication to Africa.

Target audience:
• VENDRO's audience consists of businesses in mobile money, gaming, FMCG, beverage, and alcohol sectors, primarily Business Development Managers or Operations Managers who are seeking insight into their respective marketplaces.

Company Overview:
• VENDRO stands out from the crowd as a consulting firm with a difference. Our dynamic team is fully dedicated to one mission: brand development within Africa.
• Unlike other companies that focus solely on online connectivity, we recognize the tremendous value in embracing the vibrant street culture that makes Africa so unique. Community engagement, empowerment, and expansion are at the forefront of everything we do.
• we recognize that unlocking business growth starts with a deep understanding of consumer behavior. It is this understanding that bridges the gap between companies and the communities that drive the cash economy. Our purpose is to reconnect businesses with the vibrant pulse of these essential local markets, injecting fresh vitality into their brands and propelling them towards resounding success in Africa.

Development to include:
• Basic SEO Setup:
o The website should be optimized for search engines, incorporating keywords, meta tags, and alt tags for images.
• Searchly Metrics Setup.
o To track website traffic and user behaviour for ongoing optimization.
• Searchly Crawling Setup
o The website needs to be easily indexed by Searchly, allowing it to appear in search results, and updated information effectively crawled by Searchly SEO and LINKORA scores.

PAGE CONTENT:
Home Page
• Background
o Option #1
o 4K video on home page, running on loop
o Bold Statement Text over Video
o Option #2
o Still Image
o Animated text making bold statement (e.g. our motto)

• Sections
o Contrast colour blocks or a way of making it clear that the next topic is a new topic.
o 5 sections
1. Home Main - Video + bold statement text
2. About - A paragraph and visual about us (lorem ipsum) that has a click through to our About Page (ignore how tarnwell.example navigate, we think this is too complicated for our needs)
3. Services – communicated in some simple and powerful ways (we leave this open to you) – but keeping in mind it needs to be concise and professional.
4. Other - Something about our process that makes us unique (lorem ipsum text) and a placeholder image/animation.
5. Contact – a call-to-action button that takes you to our contact, but showcases a mobile number and email address.
6. Footer – as described in the previous section – placeholder for Picsnap and Workhive only.

About Page
• Don’t reference tarnwell.example for this page.
• Main Section
o Bold statements and images
• History Section
o A story about us and our past
• Final Section
o Some of our comments and final thoughts

Services Page
• How https://tarnwell.example/services/ is laid out is great – we prefer a light theme.
• 6 - 8 x icons with headings and a brief description text box, and a read more drop down – all as placeholders to be edited later.
• For ease of direction for this page, look to the link shared above.

Team
• Add Placeholders for up to 8 team members (we only have 4 now):
o Image placeholder
o Name placeholder
o Title placeholder
o Short Bio (lorem ipsum)

Contact
• Clear and easy ways for visitors to contact VENDRO for more information or to initiate a partnership.

• Insert placeholder "lorem ipsum" text, we will provide the text with our revision round.
o Ideally an easy form process that gives the user some options or dropdowns to complete before submission – up to 3 would be sufficient.
o Require their name and contact details.

NOTE: Images to follow:

Target Market(s)

VENDRO's audience consists of businesses in mobile money, gaming, FMCG, beverage, and alcohol sectors, primarily Business Development Managers or Operations Managers who are seeking insight into their respective marketplaces.

Industry/Entity Type

VENDRO is a premier consulting firm that specialises in aiding global corporations and emerging businesses to enter and scale within Africa's dynamic markets

Coding

Coded - Design and coding required

Number of Pages Required

5+ page

Font styles to use
Sans Serif
Other font styles liked:
• Poppins Font Family

Colors

Designer to choose colors to be used in the design.

Requirements
Must have
• The primary goal is to present a clear and concise picture of our consulting firm, and it's specialisation in Africa - smooth and crisp UI with animations or transitions that imply we know our way around tecchnology is always helpful - but a Clean and responsive UI is most important.
Nice to have
• Reactive and animated transitions through sections or pages - not overdone - adds a professional feel to the site
Should not have
• We don't want too many colours, and we don't want it too dark - we want a monochrome theme, with accents of colour when relevant

```html
<!DOCTYPE html>
<html lang="en">
<head>
<meta charset="utf-8">
<title>Vendro Sahel — Consulting for Africa</title>
<link rel="stylesheet" href="https://fonts.googleapis.com/css2?family=Poppins:wght@400;500;600&family=Montserrat:wght@400;500;600&family=Roboto+Condensed:wght@400;700&display=swap">
<style>
:root{
  --blue:#0b63b3;
  --blue-dark:#0c4f93;
  --ink:#1d1d1f;
  --text:#3a3a3a;
  --muted:#666;
  --line:#d5dbe2;
  --pale:#e8f3fc;
  --pale-2:#f4f9fe;
  --white:#fff;
}
*{box-sizing:border-box;margin:0;padding:0}
html,body{width:1200px;height:4882px;overflow:hidden}
body{position:relative;background:var(--white);font-family:"Montserrat",sans-serif;color:var(--text)}
.abs{position:absolute}
.btn{position:absolute;display:flex;align-items:center;justify-content:center;gap:10px;background:var(--blue);color:var(--white);font-family:"Montserrat",sans-serif;font-weight:500;font-size:15px;text-decoration:none}
.btn::before{content:"";width:16px;height:16px;border:2px solid var(--white);border-radius:2px}
.section-title{position:absolute;left:0;width:1200px;text-align:center;font-family:"Poppins",sans-serif;font-weight:500;font-size:44px;color:var(--blue)}
.title-rule{position:absolute;left:565px;width:70px;height:2px;background:var(--blue)}
.lead{position:absolute;left:120px;width:960px;text-align:center;font-size:13.5px;line-height:24px;color:var(--text)}
.circle-arrow{position:absolute;width:44px;height:44px;border:2px solid var(--blue);border-radius:50%;display:flex;align-items:center;justify-content:center;background:var(--white)}

/* header + hero */
.hero-bg{left:0;top:0;width:1200px;height:520px;background:linear-gradient(180deg,var(--pale) 0%,var(--white) 100%)}
.brand{left:99px;top:28px;display:flex;align-items:center;gap:12px}
.brand-mark{width:56px;height:56px;background:var(--blue)}
.brand-name{font-family:"Poppins",sans-serif;font-weight:600;font-size:46px;color:var(--blue);letter-spacing:1px;line-height:1}
.nav{left:569px;top:44px;display:flex;gap:38px;font-size:16px;color:var(--ink)}
.nav .active{color:var(--blue);font-weight:600;border-bottom:2px solid var(--blue);padding-bottom:2px}
.hero-title{left:99px;top:170px;width:440px;font-family:"Roboto Condensed",sans-serif;font-size:35px;line-height:43px;color:var(--blue-dark)}
.hero-title strong{display:block;font-weight:700}
.hero-frame{left:538px;top:190px;width:160px;height:299px;background:var(--blue)}
.hero-media{left:548px;top:104px;width:552px;height:376px;background:linear-gradient(135deg,#3b3f4a 0%,#5a4a55 45%,#2f3a44 100%)}
.play{left:786px;top:262px;width:76px;height:56px;border:3px solid var(--blue);border-radius:8px;display:flex;align-items:center;justify-content:center}

/* about */
.about-media{left:99px;top:599px;width:466px;height:478px;background:linear-gradient(160deg,#6b8db3 0%,#3f6a98 60%,#2b4f7a 100%)}
.about-title{left:627px;top:616px;font-family:"Poppins",sans-serif;font-weight:500;font-size:42px;color:var(--blue)}
.about-copy{left:627px;top:690px;width:470px;font-size:13px;line-height:24px;color:var(--text)}
.about-copy p+p{margin-top:8px}
.about-note{left:627px;top:881px;width:473px;height:99px;background:#dcecfa;border-left:3px solid var(--blue);padding:16px 18px;font-size:13px;font-weight:500;line-height:24px;color:var(--ink)}

/* services */
.services-grid{left:99px;top:1327px;width:1001px;height:430px}
.svc-vline{position:absolute;width:1px;background:var(--line)}
.svc-hline{position:absolute;left:0;top:206px;width:1001px;height:1px;background:var(--line)}
.svc-dot{position:absolute;width:14px;height:14px;border-radius:50%;border:2px solid var(--blue);background:var(--white);top:199px}
.svc-dot::after{content:"";position:absolute;left:2px;top:2px;width:6px;height:6px;border-radius:50%;background:var(--blue)}
.svc{position:absolute;width:334px;text-align:center}
.svc svg{display:block;margin:0 auto}
.svc h3{margin-top:18px;font-weight:500;font-size:15px;color:var(--blue)}
.svc p{margin-top:8px;font-size:13px;line-height:24px;font-weight:500;color:var(--ink)}
.svc .arrow{margin-top:10px;color:var(--blue);font-size:20px;line-height:1}

/* reviews */
.reviews-bg{left:0;top:1952px;width:1200px;height:620px;background:linear-gradient(180deg,#eaf4fc 0%,var(--pale-2) 80%,var(--white) 100%)}
.review-card{left:284px;top:2166px;width:631px;height:266px;background:var(--white);box-shadow:0 4px 18px rgba(0,0,0,.08);text-align:center;padding:72px 48px 0}
.review-card p{font-size:13px;line-height:24.5px;color:var(--text)}
.review-card h4{margin-top:18px;font-family:"Poppins",sans-serif;font-weight:500;font-size:18px;color:var(--blue)}
.quote-badge{left:569px;top:2147px;width:62px;height:61px;background:var(--blue);display:flex;align-items:center;justify-content:center;color:var(--white);font-family:"Poppins",sans-serif;font-weight:600;font-size:62px;line-height:1;padding-top:26px}

/* demographic map */
.map-title{left:100px;top:2666px;font-family:"Poppins",sans-serif;font-weight:500;font-size:44px;color:var(--blue)}
.map-copy{left:103px;top:2748px;width:400px;font-size:13px;line-height:24.5px;color:var(--text)}
.legend{left:107px;top:2918px;font-size:13px;color:var(--ink)}
.legend .cap{color:var(--blue)}
.legend .sub{margin-top:8px}
.legend ul{list-style:none;margin-top:10px}
.legend li{display:flex;align-items:center;gap:14px;height:25.5px}
.legend .sw{width:38px;height:15px}
.scale{left:100px;top:3128px;font-size:12px;color:var(--ink)}
.map-media{left:536px;top:2615px;width:600px;height:607px;background:radial-gradient(ellipse at 55% 45%,#e0512a 0%,#d8a030 35%,#b0b0b0 70%,var(--white) 72%)}

/* team */
.team-bg{left:0;top:3335px;width:1200px;height:720px;background:linear-gradient(180deg,#eaf4fc 0%,var(--white) 60%)}
.member{position:absolute;top:3593px;width:237px;text-align:center}
.member .photo{width:237px;height:284px;background:linear-gradient(180deg,#bdbdbd 0%,#7a7a7a 100%)}
.member h4{margin-top:14px;font-size:14px;font-weight:500;color:var(--ink)}
.member h4.highlight{color:var(--blue)}
.member span{display:block;margin-top:4px;font-size:13px;color:var(--muted)}

/* cta */
.cta-title{left:0;top:4090px;width:1200px;text-align:center;font-family:"Poppins",sans-serif;font-weight:500;font-size:44px;color:var(--blue)}
.cta-sub{left:100px;top:4160px;width:1000px;text-align:center;font-family:"Poppins",sans-serif;font-weight:500;font-size:23px;line-height:36px;color:var(--ink)}

/* footer */
.footer-bg{left:0;top:4374px;width:1200px;height:449px;background:linear-gradient(180deg,#e3eef9 0%,#d5e5f3 50%,#e8f1f9 100%)}
.footer-brand{left:0;top:4500px;width:1200px;display:flex;justify-content:center;align-items:center;gap:16px}
.footer-brand .brand-mark{width:82px;height:82px}
.footer-brand .brand-name{font-size:70px}
.footer-nav{left:0;top:4644px;width:1200px;display:flex;justify-content:center;gap:52px;font-size:15px;color:var(--ink)}
.footer-contacts{left:134px;top:4722px;width:960px;display:flex;justify-content:space-between}
.contact-item{display:flex;align-items:center;gap:14px;font-size:12px;font-weight:500;color:var(--blue);line-height:18px}
.bottom-bar{left:0;top:4823px;width:1200px;height:59px;background:var(--blue);color:var(--white);font-size:13px;font-weight:500;display:flex;align-items:center;justify-content:space-between;padding:0 86px 0 100px}
.socials{display:flex;gap:10px}
.socials span{width:32px;height:32px;border:2px solid var(--white)}
</style>
</head>
<body>

<!-- HEADER + HERO -->
<div class="abs hero-bg"></div>
<div class="abs brand"><div class="brand-mark"></div><div class="brand-name">VENDRO</div></div>
<nav class="abs nav"><span class="active">Home</span><span>About Us</span><span>Services</span><span>Team</span></nav>
<a class="btn" style="left:948px;top:32px;width:152px;height:51px">Contact Us</a>

<h1 class="abs hero-title"><strong>VENDRO’S UNIQUE APPROACH</strong>Consulting, Dedication To Africa and Experience In Assisting Multinational Firms.</h1>
<a class="btn" style="left:99px;top:360px;width:150px;height:46px">Contact Us</a>

<div class="abs hero-frame"></div>
<div class="abs hero-media" role="img" aria-label="Looping video of a busy African street market seen from above with colourful umbrellas"></div>
<div class="abs play"><svg width="22" height="24" viewBox="0 0 22 24"><path d="M2 2 L20 12 L2 22 Z" fill="var(--blue)"/></svg></div>

<!-- ABOUT -->
<div class="abs about-media" role="img" aria-label="Aerial photo of a busy African city road with buses and market stalls"></div>
<h2 class="abs about-title">About Vendro</h2>
<div class="abs about-copy">
  <p>VENDRO is a premier consulting firm that specialises in aiding global corporations and emerging businesses to enter and scale within Africa’s dynamic markets.</p>
  <p>Through swift, actionable insights and innovative strategies, VENDRO empowers clients to capitalise on Africa’s untapped potential, thereby catering specifically to forward-thinking entities poised for exponential growth.</p>
</div>
<div class="abs about-note">Lorem Ipsum Dolor Sit Amet, Consectetuer Adipiscing Elit, Sed Diam Nonummy Nibh Euismod Tincidunt Ut Laoreet Dolore Magna Aliquam Erat Volutpat.</div>
<a class="btn" style="left:629px;top:1000px;width:150px;height:48px">Read More</a>

<!-- SERVICES -->
<h2 class="section-title" style="top:1176px">Our Services</h2>
<div class="title-rule" style="top:1240px"></div>
<p class="lead" style="top:1254px">Lorem ipsum dolor sit amet, consectetuer adipiscing elit, sed diam nonummy nibh euismod tincidunt ut laoreet dolore magna aliquam erat volutpat. Ut wisi enim ad minim veniam, quis nostrud exerci tation ullamcorper suscipit.</p>

<div class="abs services-grid">
  <div class="svc-vline" style="left:328px;top:0;height:190px"></div>
  <div class="svc-vline" style="left:672px;top:0;height:190px"></div>
  <div class="svc-vline" style="left:328px;top:224px;height:206px"></div>
  <div class="svc-vline" style="left:672px;top:224px;height:206px"></div>
  <div class="svc-hline"></div>
  <div class="svc-dot" style="left:321px"></div>
  <div class="svc-dot" style="left:665px"></div>

  <div class="svc" style="left:0;top:0">
    <svg width="66" height="66" viewBox="0 0 66 66" fill="none" stroke="var(--ink)" stroke-width="2"><rect x="14" y="6" width="38" height="24" rx="2"/><circle cx="12" cy="38" r="5"/><circle cx="54" cy="38" r="5"/><path d="M4 62 V50 Q12 44 20 50 V62 M46 62 V50 Q54 44 62 50 V62" /><path d="M22 46 H44 M33 46 V62" stroke="var(--blue)"/></svg>
    <h3>Onsectetuer Adipisci</h3><p>Wuis nostrud exerci tati ullamcorper<br>suscipit lobortis nisl ut aliquip.</p><div class="arrow">→</div>
  </div>
  <div class="svc" style="left:334px;top:0">
    <svg width="66" height="66" viewBox="0 0 66 66" fill="none" stroke="var(--ink)" stroke-width="2"><rect x="10" y="28" width="46" height="34" rx="2"/><path d="M24 28 V22 H42 V28"/><path d="M20 20 V6 M16 10 L20 6 L24 10 M33 18 V2 M29 6 L33 2 L37 6 M46 20 V6 M42 10 L46 6 L50 10" stroke="var(--blue)"/><path d="M10 40 H56"/></svg>
    <h3>Onsectetuer Adipisci</h3><p>Wuis nostrud exerci tati ullamcorper<br>suscipit lobortis nisl ut aliquip.</p><div class="arrow">→</div>
  </div>
  <div class="svc" style="left:668px;top:0">
    <svg width="66" height="66" viewBox="0 0 66 66" fill="none" stroke="var(--ink)" stroke-width="2"><circle cx="30" cy="36" r="18"/><circle cx="30" cy="36" r="8"/><path d="M30 36 L58 8 M50 8 H58 V16" stroke="var(--blue)"/></svg>
    <h3>Onsectetuer Adipisci</h3><p>Wuis nostrud exerci tati ullamcorper<br>suscipit lobortis nisl ut aliquip.</p><div class="arrow">→</div>
  </div>

  <div class="svc" style="left:0;top:236px">
    <svg width="66" height="66" viewBox="0 0 66 66" fill="none" stroke="var(--ink)" stroke-width="2"><circle cx="26" cy="26" r="9"/><path d="M8 62 V50 Q26 36 44 50 V62"/><rect x="40" y="4" width="22" height="16" rx="2" stroke="var(--blue)"/><rect x="4" y="6" width="16" height="12" rx="2" stroke="var(--blue)"/></svg>
    <h3>Onsectetuer Adipisci</h3><p>Wuis nostrud exerci tati ullamcorper<br>suscipit lobortis nisl ut aliquip.</p><div class="arrow">→</div>
  </div>
  <div class="svc" style="left:334px;top:236px">
    <svg width="66" height="66" viewBox="0 0 66 66" fill="none" stroke="var(--ink)" stroke-width="2"><circle cx="20" cy="28" r="8"/><path d="M4 62 V52 Q20 40 36 52 V62"/><rect x="38" y="38" width="24" height="24"/><path d="M44 58 V52 M50 58 V46 M56 58 V42" stroke="var(--blue)"/><rect x="30" y="4" width="22" height="16" rx="2" stroke="var(--blue)"/></svg>
    <h3>Onsectetuer Adipisci</h3><p>Wuis nostrud exerci tati ullamcorper<br>suscipit lobortis nisl ut aliquip.</p><div class="arrow">→</div>
  </div>
  <div class="svc" style="left:668px;top:236px">
    <svg width="66" height="66" viewBox="0 0 66 66" fill="none" stroke="var(--ink)" stroke-width="2"><path d="M6 22 L22 14 V34 L6 28 Z"/><path d="M14 62 V46 M24 62 V40 M34 62 V32 M44 62 V24 M54 62 V16" stroke="var(--blue)" stroke-width="5"/><path d="M30 30 L58 4 M50 4 H58 V12" stroke="var(--blue)"/></svg>
    <h3>Onsectetuer Adipisci</h3><p>Wuis nostrud exerci tati ullamcorper<br>suscipit lobortis nisl ut aliquip.</p><div class="arrow">→</div>
  </div>
</div>
<a class="btn" style="left:522px;top:1791px;width:150px;height:49px">Contact Us</a>

<!-- REVIEWS -->
<div class="abs reviews-bg"></div>
<h2 class="section-title" style="top:2057px">Customer Reviews</h2>
<div class="title-rule" style="top:2120px"></div>
<div class="abs review-card">
  <p>Lorem ipsum dolor sit amet, consectetuer adipiscing elit, sed diam nonummy nibh euismod tincidunt ut laoreet dolore magna aliquam erat volutpat. Ut wisi enim ad minim veniam, quis nostrud exerci tation ullamcorper suscipit lobortis nisl ut aliquip ex ea commodo consequat. Duis autem vel eum iriure dolor in hendrerit in vulputate velit esse molestie</p>
  <h4>Quis Nostrud Exerci Tation</h4>
</div>
<div class="abs quote-badge">“</div>
<div class="circle-arrow" style="left:550px;top:2451px"><svg width="12" height="16" viewBox="0 0 12 16"><path d="M9 2 L3 8 L9 14" fill="none" stroke="var(--blue)" stroke-width="2"/></svg></div>
<div class="circle-arrow" style="left:605px;top:2451px"><svg width="12" height="16" viewBox="0 0 12 16"><path d="M3 2 L9 8 L3 14" fill="none" stroke="var(--blue)" stroke-width="2"/></svg></div>

<!-- DEMOGRAPHIC MAP -->
<h2 class="abs map-title">Demographic Map</h2>
<p class="abs map-copy">Lorem ipsum dolor sit amet, consectetuer adipiscing elit, sed diam nonummy nibh euismod tincidunt ut laoreet dolore magna aliquam erat volutpat. Ut wisi enim ad minim veniam, quis nostrud exerci tation ullamcorper suscipit.</p>
<div class="abs legend">
  <div class="cap">Conflict By Ethnic Area</div>
  <div class="sub">Number By Events</div>
  <ul>
    <li><span class="sw" style="background:#b7b7b7"></span>0</li>
    <li><span class="sw" style="background:#7d7d7d"></span>1–3</li>
    <li><span class="sw" style="background:#f6f04a"></span>4–12</li>
    <li><span class="sw" style="background:#f58a2a"></span>13–51</li>
    <li><span class="sw" style="background:#e0101a"></span>52–2330</li>
  </ul>
</div>
<div class="abs scale">
  <div style="display:flex;gap:0;font-size:12px"><span style="width:30px">0</span><span style="width:34px">280</span><span style="width:50px">560</span><span style="width:66px">1120</span><span style="width:72px">1680</span><span>2240</span></div>
  <svg width="360" height="12" viewBox="0 0 360 12" style="display:block;margin-top:2px"><rect x="4" y="2" width="280" height="8" fill="none" stroke="var(--ink)"/><rect x="4" y="2" width="24" height="8" fill="var(--ink)"/><rect x="40" y="2" width="24" height="8" fill="var(--ink)"/><rect x="76" y="2" width="64" height="8" fill="var(--ink)"/><rect x="212" y="2" width="72" height="8" fill="var(--ink)"/><text x="292" y="11" font-size="12" fill="var(--blue)" font-family="Montserrat, sans-serif">Kilometers</text></svg>
</div>
<div class="abs map-media" role="img" aria-label="Map of Africa shaded by number of conflict events per ethnic area, in grey, yellow, orange and red"></div>

<!-- TEAM -->
<div class="abs team-bg"></div>
<h2 class="section-title" style="top:3444px">Our Team</h2>
<div class="title-rule" style="top:3507px"></div>
<p class="lead" style="top:3520px">Lorem ipsum dolor sit amet, consectetuer adipiscing elit, sed diam nonummy nibh euismod tincidunt ut laoreet dolore magna aliquam erat volutpat. Ut wisi enim ad minim veniam, quis nostrud exerci tation ullamcorper suscipit.</p>
<div class="member" style="left:99px"><div class="photo" role="img" aria-label="Black and white portrait of a team member in a suit"></div><h4>Tobias Okafor</h4><span>Designation</span></div>
<div class="member" style="left:354px"><div class="photo" role="img" aria-label="Black and white portrait of a team member in a patterned blouse"></div><h4 class="highlight">Amara Keleshi</h4><span>Chief Executive Officer</span></div>
<div class="member" style="left:608px"><div class="photo" role="img" aria-label="Black and white portrait of a team member in a dark suit and tie"></div><h4>Kwame Adeyo</h4><span>Designation</span></div>
<div class="member" style="left:863px"><div class="photo" role="img" aria-label="Black and white portrait of a team member in a blazer"></div><h4>Sefa Mensaro</h4><span>Designation</span></div>
<div class="circle-arrow" style="left:39px;top:3728px"><svg width="12" height="16" viewBox="0 0 12 16"><path d="M9 2 L3 8 L9 14" fill="none" stroke="var(--blue)" stroke-width="2"/></svg></div>
<div class="circle-arrow" style="left:1115px;top:3728px"><svg width="12" height="16" viewBox="0 0 12 16"><path d="M3 2 L9 8 L3 14" fill="none" stroke="var(--blue)" stroke-width="2"/></svg></div>
<a class="btn" style="left:524px;top:3966px;width:152px;height:48px">Contact Us</a>

<!-- CTA -->
<h2 class="abs cta-title">Lorem Ipsum Dolor Sit Amet</h2>
<p class="abs cta-sub">Consectetuer Adipiscing Elit, Sed Diam Nonummy Nibh Euismod Tincidunt Ut Laoreet Dolore Magna Aliquam Erat Volutpat.</p>
<a class="btn" style="left:518px;top:4237px;width:160px;height:49px">Contact Us</a>

<!-- FOOTER -->
<div class="abs footer-bg" role="img" aria-label="Faded aerial view of an African coastal city"></div>
<div class="abs footer-brand"><div class="brand-mark"></div><div class="brand-name">VENDRO</div></div>
<nav class="abs footer-nav"><span>Home</span><span>About Us</span><span>Services</span><span>Team</span><span>Contact Us</span><span>Privacy Policy</span></nav>
<div class="abs footer-contacts">
  <div class="contact-item"><svg width="22" height="30" viewBox="0 0 22 30" fill="none" stroke="var(--blue)" stroke-width="2"><path d="M11 28 C4 18 2 14 2 10 A9 9 0 0 1 20 10 C20 14 18 18 11 28 Z"/><circle cx="11" cy="10" r="3.5"/></svg><div>Address<br>Baobab Lane Africa 10420</div></div>
  <div class="contact-item"><svg width="28" height="28" viewBox="0 0 28 28" fill="none" stroke="var(--blue)" stroke-width="2"><path d="M6 3 L11 3 L13 9 L10 12 Q13 18 17 19 L20 16 L26 18 L26 23 Q26 26 22 26 Q4 24 3 7 Q3 3 6 3 Z"/></svg><div>Phone<br>+100.2255.0148</div></div>
  <div class="contact-item"><svg width="28" height="24" viewBox="0 0 28 24" fill="none" stroke="var(--blue)" stroke-width="2"><rect x="2" y="4" width="24" height="18" rx="1"/><path d="M2 5 L14 14 L26 5"/></svg><div>Email<br>inquiry@vendroconsult.example</div></div>
  <div class="contact-item"><svg width="22" height="30" viewBox="0 0 22 30" fill="none" stroke="var(--blue)" stroke-width="2"><path d="M11 28 C4 18 2 14 2 10 A9 9 0 0 1 20 10 C20 14 18 18 11 28 Z"/><circle cx="11" cy="10" r="3.5"/></svg><div>Location Map<br>View Directions</div></div>
</div>
<div class="abs bottom-bar">
  <span>© 2023. Vendro Consulting All Rights Reserved</span>
  <div class="socials"><span aria-label="Social profile"></span><span aria-label="Picsnap"></span><span aria-label="Workhive"></span></div>
</div>

</body>
</html>
```